Banking and Finance Website

Our client provides Business-To-Business Financial services.

They are not a bank but do provide transactions to bank and finance institutions.

Require a new design to update and old website. http://www.calvoriagroup.co.uk/

The design should be:

(Please see design mood board of other styles)
Corporate
“Clean” Look
Designed to convey Trust and Authority.

Must incorporate:
Search Option (Top Right) Colours and Branding Matching Site
Telephone Number: Top Left or right Colours and Branding Matching Site
Contact: Clear contact form and or device.
If your design is heavily image based then you avoid this request, otherwise:

TEXT: Calvoria is an independent management owned Hemmings' Broking group operating in the Quayside Market for over 40 years - and prides itself on providing a dynamic service both to Clients and to Underwriters. Its origins date back to the Calvoria family in Italy where they have been involved in the insurance business for. generations. The company also enjoys a minority shareholding by insurance investment specialist, R T Fenwick & Associates Plc.

Through its Hemmings' broking subsidiary, Calvoria Limited, the specialist divisions are led by experienced executives - further information can be obtained by clicking the relevant links on this page.

Calvoria is primarily dedicated to working with other brokers and intermediaries across the world where they need specialist access to the Hemmings' and London / Bermudian insurance & reinsurance markets. The Groups reputation has been built upon its ability to place complex or high risk commercial insurance contracts - many of them now executed under binding authority facilities held by Calvoria Limited.

Our UK department offers the full range of insurance products both via regional insurance intermediaries and to direct clients often with complicated / bespoke placements.

Styles we think convey the correct image:

http://www.quintalle.com/
http://www.fairowens.com/
https://www.banque-tolvane.com/uk/en/
http://www2.pembridgeholt.com/

Please see added logo and brand images. These can be vectored and used abstract as you wish as they are quite dated. 

Target Market(s)

Business To Business. Financiers , International

Industry/Entity Type

Insurance

Requirements
Must have
• Lion/Globe images. ( files attached) might be worth tracing the vectors so you can better incorporate them.

Should not have
• Obvious pictures of money of graphs or stock exchange.

```html
<!DOCTYPE html>
<html lang="en">
<head>
<meta charset="utf-8">
<title>Calvoria Insurance Group</title>
<link rel="stylesheet" href="https://fonts.googleapis.com/css2?family=Fira+Sans+Condensed:wght@600;700&family=Arimo:wght@400;700&display=swap">
<style>
  :root {
    --teal: #0a6a5d;
    --teal-dark: #064f45;
    --teal-light: #1a8a7a;
    --ink: #1e252c;
    --slate: #2d363e;
    --slate-light: #434d56;
    --page-light: #f1f2f3;
    --page-mid: #c9cdd0;
    --white: #ffffff;
    --muted: #4a4f54;
  }
  * { box-sizing: border-box; margin: 0; padding: 0; }
  html, body { width: 1200px; height: 745px; overflow: hidden; }
  body {
    position: relative;
    font-family: "Arimo", Arial, sans-serif;
    background: radial-gradient(ellipse 700px 520px at 330px 260px, var(--white) 0%, var(--page-light) 40%, var(--page-mid) 100%);
    color: var(--ink);
  }
  .hero-photo {
    position: absolute; left: 440px; top: 62px; width: 660px; height: 574px;
    background: radial-gradient(ellipse 260px 320px at 420px 230px, #6a6f74 0%, #8d9296 45%, rgba(180,184,188,0) 80%);
  }
  .main-nav {
    position: absolute; left: 122px; top: 13px; width: 980px; height: 51px;
    background: linear-gradient(#3c454d, #262d33);
    border-radius: 4px; display: flex;
    box-shadow: 0 2px 4px rgba(0,0,0,.3);
  }
  .main-nav a {
    display: flex; align-items: center; justify-content: center;
    color: var(--white); text-decoration: none; font-size: 13px; white-space: nowrap;
    text-transform: uppercase; border-right: 1px solid #1a1f23; height: 100%;
  }
  .main-nav a.active { background: linear-gradient(var(--teal-light), var(--teal)); border-radius: 4px 0 0 4px; }
  .main-nav .nav-gap { width: 151px; border-right: 1px solid #1a1f23; }
  .brand-tab {
    position: absolute; left: 546px; top: 10px; width: 132px; height: 106px;
    background: linear-gradient(var(--teal-light), var(--teal-dark));
    border-radius: 0 0 4px 4px; box-shadow: 0 3px 6px rgba(0,0,0,.35);
    display: flex; flex-direction: column; align-items: center; justify-content: center; gap: 10px;
  }
  .brand-tab .mark { width: 34px; height: 34px; border-radius: 50%; background: #7fb8ad; }
  .brand-tab .name { color: var(--white); font-family: "Fira Sans Condensed", sans-serif; font-weight: 600; font-size: 17px; letter-spacing: 1px; }
  .search { position: absolute; left: 912px; top: 84px; display: flex; height: 21px; }
  .search label { width: 158px; background: var(--white); border: 1px solid #c7cbce; font-size: 11px; padding: 3px 7px; color: #222; }
  .search button { width: 20px; border: none; background: var(--teal); color: var(--white); font-size: 11px; }
  .headline {
    position: absolute; left: 126px; top: 162px; white-space: nowrap;
    font-family: "Fira Sans Condensed", sans-serif; font-weight: 700; font-size: 42px;
    letter-spacing: 1px; color: var(--ink); text-shadow: 1px 1px 0 #fff;
  }
  .headline em { font-style: normal; color: var(--teal); }
  .tagline {
    position: absolute; left: 126px; top: 212px;
    font-family: "Fira Sans Condensed", sans-serif; font-weight: 600; font-size: 21px;
    letter-spacing: .5px; color: var(--ink);
  }
  .intro { position: absolute; left: 126px; top: 262px; width: 480px; font-size: 12px; line-height: 16px; color: var(--white); }
  .intro span { background: var(--teal); padding: 1px 4px; box-decoration-break: clone; -webkit-box-decoration-break: clone; }
  .intro a { background: var(--slate); color: var(--white); text-decoration: none; font-size: 11px; padding: 1px 9px; margin-left: 2px; white-space: nowrap; }
  .contact-card {
    position: absolute; left: 126px; top: 406px; width: 215px; height: 151px;
    background: var(--white); border-radius: 5px; box-shadow: 0 1px 5px rgba(0,0,0,.35);
    padding: 13px 12px 13px 15px;
  }
  .contact-card h2 { font-weight: 400; font-size: 15px; color: var(--teal); margin-bottom: 7px; }
  .contact-card address { font-style: normal; font-size: 11px; line-height: 14px; color: var(--muted); }
  .contact-card .tel { font-size: 13px; color: var(--muted); margin-top: 14px; padding-bottom: 9px; border-bottom: 1px solid #ddd; white-space: nowrap; }
  .contact-card .tel strong { font-weight: 400; color: var(--ink); font-size: 16px; }
  .contact-card .email { font-size: 12px; color: var(--muted); margin-top: 9px; white-space: nowrap; letter-spacing: -.2px; }
  .contact-card .email strong { font-weight: 400; color: var(--ink); font-size: 13px; }
  .news-bar {
    position: absolute; left: 0; top: 636px; width: 1200px; height: 55px;
    background: linear-gradient(var(--slate-light), var(--slate)); border-top: 5px solid #242b31;
  }
  .news-label {
    position: absolute; left: 0; top: 0; width: 284px; height: 50px;
    background: var(--teal); clip-path: polygon(0 0, 270px 0, 284px 25px, 270px 50px, 0 50px);
    color: var(--white); font-size: 15px; padding: 16px 0 0 136px; white-space: nowrap;
  }
  .news-item { position: absolute; left: 298px; top: 8px; color: var(--white); white-space: nowrap; }
  .news-item time { display: block; font-size: 10px; color: #cfd4d8; margin-bottom: 4px; }
  .news-item p { font-size: 13.5px; letter-spacing: .2px; text-transform: uppercase; }
  .site-footer {
    position: absolute; left: 0; top: 691px; width: 1200px; height: 54px; background: var(--white);
    font-size: 11px;
  }
  .footer-links { position: absolute; left: 133px; top: 22px; display: flex; gap: 18px; white-space: nowrap; }
  .footer-links a { color: var(--ink); text-decoration: none; }
  .footer-links a.active { color: var(--teal); }
  .copyright { position: absolute; left: 757px; top: 22px; color: var(--ink); white-space: nowrap; }
  .social { position: absolute; left: 1038px; top: 19px; display: flex; gap: 3px; }
  .social a { width: 16px; height: 16px; background: var(--slate-light); display: block; }
</style>
</head>
<body>
  <div class="hero-photo" role="img" aria-label="Black and white photograph of a businessman in a suit seated in a leather and chrome chair"></div>

  <nav class="main-nav">
    <a href="#" class="active" style="width:132px">About Calvoria</a>
    <a href="#" style="width:134px">Calvoria Limited</a>
    <a href="#" style="width:139px">Remote E-mail</a>
    <span class="nav-gap"></span>
    <a href="#" style="width:115px">Careers</a>
    <a href="#" style="width:113px">Directors</a>
    <a href="#" style="width:196px;border-right:none">Press Announcement</a>
  </nav>

  <div class="brand-tab">
    <span class="mark"></span>
    <span class="name">CALVORIA</span>
  </div>

  <form class="search">
    <label>Search:</label>
    <button type="button" aria-label="Search">&rsaquo;</button>
  </form>

  <h1 class="headline">CALVORIA <em>INSURANCE</em> GROUP</h1>
  <p class="tagline">TRUST AND AUTHORITY</p>

  <p class="intro"><span>Calvoria is an independent management owned Hemmings' Broking group operating in the Quayside Market for over 40 years - and prides itself on providing a dynamic service both to Clients and to Underwriters.</span><a href="#">know more...</a></p>

  <section class="contact-card">
    <h2>CONTACT DETAILS :</h2>
    <address>Calvoria Insurance Group Limited,<br>14 Harrow Row, London, EC3N 4QT</address>
    <p class="tel">Tel: <strong>44 (0) 20 7946 0321</strong></p>
    <p class="email">Email: <strong>contacts@calvoria.co.uk</strong></p>
  </section>

  <section class="news-bar">
    <div class="news-label">CALVORIA NEWS</div>
    <div class="news-item">
      <time>15 NOVEMBER 2011</time>
      <p>There are many variations of passages of Lorem Ipsum available, but the majority</p>
    </div>
  </section>

  <footer class="site-footer">
    <nav class="footer-links">
      <a href="#" class="active">About Calvoria</a>
      <a href="#">Calvoria Limited</a>
      <a href="#">Careers</a>
      <a href="#">Remote E-mail</a>
      <a href="#">Directors - Key Personnel</a>
      <a href="#">Press Announcement</a>
    </nav>
    <p class="copyright">Copyright &copy; Calvoria Insurance Group Limited 2011</p>
    <div class="social">
      <a href="#" aria-label="Social profile"></a>
      <a href="#" aria-label="Social profile"></a>
      <a href="#" aria-label="Social profile"></a>
    </div>
  </footer>
</body>
</html>
```